The Morrow Ledgers Website

I need a website to help promote the series of science fiction novels that I am in the process of writing.

I have some content and photos and am in the process of getting some new book cover artwork designed.

I have a current website/domain etc http://www.vantorpagehouse.co.nz but I need something a little more professional and eye catchig but I also want to be able to manage the content myself.

I can send e-versions of the two completed novels for context to any takers

```html
<!DOCTYPE html>
<html lang="en">
<head>
<meta charset="utf-8">
<title>The Morrow Ledgers</title>
<link rel="stylesheet" href="https://fonts.googleapis.com/css2?family=Open+Sans:wght@600;700&family=Oswald:wght@400&display=swap">
<style>
  :root {
    --white: #ffffff;
    --ink: #1c1c1c;
    --nav-ink: #111111;
    --accent-blue: #1b9be0;
    --buy-green: #9bcb62;
    --logo-square: #8cc63f;
    --night-top: #1d2a47;
    --night-mid: #2b3f66;
    --night-low: #141c2e;
    --cover-light: #a6d65a;
    --cover-dark: #6fae35;
  }
  * { margin: 0; padding: 0; box-sizing: border-box; }
  html, body { width: 1200px; height: 900px; overflow: hidden; background: var(--white); }
  body { font-family: "Open Sans", Arial, sans-serif; color: var(--ink); position: relative; }

  .site-header { position: absolute; top: 0; left: 0; width: 1200px; height: 110px; background: var(--white); }
  .brand { position: absolute; left: 101px; top: 20px; display: flex; align-items: center; gap: 10px; }
  .brand-mark { width: 68px; height: 68px; background: var(--logo-square); }
  .brand-name { font-weight: 700; font-size: 19px; line-height: 22px; color: var(--ink); width: 100px; }

  .main-nav { position: absolute; top: 37px; right: 80px; display: flex; align-items: center; }
  .main-nav a { font-family: "Oswald", Arial, sans-serif; font-size: 18px; color: var(--nav-ink); text-decoration: none; height: 40px; line-height: 40px; padding: 0 16px; margin-left: 9px; border-radius: 4px; }
  .main-nav a.is-current { background: var(--accent-blue); color: var(--white); }

  .hero { position: absolute; top: 110px; left: 0; width: 1200px; height: 690px; overflow: hidden; }
  .hero-backdrop { position: absolute; inset: 0; background: linear-gradient(180deg, var(--night-top) 0%, var(--night-mid) 45%, var(--night-low) 100%); }
  .hero-title { position: absolute; left: 102px; top: 112px; font-size: 53px; font-weight: 700; color: var(--white); letter-spacing: 0.3px; }
  .hero-blurb { position: absolute; left: 102px; top: 213px; width: 530px; font-size: 25.5px; line-height: 37.6px; font-weight: 600; color: var(--white); }
  .buy-button { position: absolute; left: 102px; top: 530px; width: 253px; height: 82px; background: var(--buy-green); border: 2px solid var(--white); border-radius: 9px; color: var(--white); font-size: 30px; font-weight: 600; text-align: center; line-height: 78px; text-decoration: none; }
  .book-cover { position: absolute; left: 686px; top: 38px; }

  .reviews-heading { position: absolute; left: 99px; top: 832px; font-family: "Oswald", Arial, sans-serif; font-weight: 400; font-size: 34px; color: var(--ink); }
</style>
</head>
<body>
  <header class="site-header">
    <div class="brand">
      <span class="brand-mark"></span>
      <span class="brand-name">The Morrow Ledgers</span>
    </div>
    <nav class="main-nav">
      <a class="is-current" href="#">Home</a>
      <a href="#">Reviews</a>
      <a href="#">About</a>
      <a href="#">Blog</a>
      <a href="#">Contact</a>
      <a href="#">Links</a>
    </nav>
  </header>

  <section class="hero">
    <div class="hero-backdrop" role="img" aria-label="Night-time futuristic city skyline with a saucer-topped tower and searchlights"></div>
    <h1 class="hero-title">The First Chronicle</h1>
    <p class="hero-blurb">Morrow is an imaginative science fiction novel of considerable skill that pokes fun at all forms of political correctness, while also indicating there are dangerous signs of a disintegrating world that is not adequately taken care of. Readers will recognise these as parallels to life on earth.</p>
    <a class="buy-button" href="#">BUY NOW</a>
    <svg class="book-cover" width="310" height="620" viewBox="0 0 310 620" role="img" aria-label="Book cover of The First Chronicle shown standing at an angle">
      <defs>
        <linearGradient id="coverFill" x1="0" y1="0" x2="1" y2="1">
          <stop offset="0" stop-color="var(--cover-light)"/>
          <stop offset="1" stop-color="var(--cover-dark)"/>
        </linearGradient>
      </defs>
      <polygon points="256,2 304,38 304,604 274,616 270,30" fill="#e9ecef"/>
      <polygon points="2,62 260,2 274,616 10,560" fill="url(#coverFill)"/>
    </svg>
  </section>

  <h2 class="reviews-heading">Reviews for the The First Chronicle</h2>
</body>
</html>
```